I need to make a car magnet

It needs to include the words "KLAVO TOUR" and "2026 MEMBER" as well as the attached silhouette of the golfer. The color scheme needs to be navy, red and white. The shape and dimensions are open for interpretation

```html
<!DOCTYPE html>
<html lang="en">
<head>
<meta charset="utf-8">
<title>KLAVO TOUR – Car Magnet Options</title>
<link rel="stylesheet" href="https://fonts.googleapis.com/css2?family=Alfa+Slab+One&family=Montserrat:wght@500;700;800&display=swap">
<style>
  :root {
    --navy: #253870;
    --red: #cf2a2b;
    --white: #ffffff;
    --sheet: #d1d1d1;
    --spec: #1f6a8a;
  }
  * { margin: 0; padding: 0; box-sizing: border-box; }
  html, body { width: 1200px; height: 2520px; overflow: hidden; }
  body { background: var(--sheet); position: relative; font-family: "Montserrat", sans-serif; }

  .spec-label {
    position: absolute; left: 0; top: 136px; width: 1200px;
    text-align: center; padding-left: 10px;
    font-family: "Montserrat", sans-serif; font-weight: 500;
    font-size: 48px; color: var(--spec); letter-spacing: 1px; line-height: 1;
  }

  .magnet {
    position: absolute; left: 247px; width: 705px; height: 529px; overflow: hidden;
  }
  .magnet--one   { top: 213px; background: var(--white); }
  .magnet--two   { top: 786px; background: var(--navy); }
  .magnet--three { top: 1357px; background: var(--navy); }
  .magnet--four  { top: 1927px; background: var(--navy); }

  .band { position: absolute; left: 0; width: 100%; }
  .band--navy-base  { top: 377px; height: 152px; background: var(--navy); }
  .band--white-base { top: 377px; height: 152px; background: var(--white); }
  .band--white-short { top: 378px; height: 129px; background: var(--white); }
  .band--navy-edge { top: 507px; height: 22px; background: var(--navy); }
  .band--red-edge  { top: 507px; height: 22px; background: var(--red); }

  .title { position: absolute; left: 59px; top: 92px; line-height: 1; font-weight: 400; }
  .title--slab {
    font-family: "Alfa Slab One", serif; font-weight: 400; font-size: 93px; letter-spacing: 0;
  }
  .title--sans {
    font-family: "Montserrat", sans-serif; font-weight: 800; font-size: 97px; letter-spacing: -2px;
  }
  .title .line { display: block; height: 105px; }
  .title--navy { color: var(--navy); }
  .title--white { color: var(--white); }

  .member-year {
    position: absolute; left: 59px; top: 410px;
    font-weight: 800; font-size: 86px; line-height: 1; color: var(--white); letter-spacing: -1px;
  }
  .member-year sup {
    font-size: 24px; font-weight: 700; letter-spacing: 1px;
    position: relative; top: -44px; margin-left: 6px; vertical-align: baseline;
  }
  .member-line {
    position: absolute; left: 59px; top: 428px;
    font-weight: 700; font-size: 44px; line-height: 1; color: var(--navy); letter-spacing: 1px;
  }

  .golfer-art {
    position: absolute; left: 455px; top: 57px; width: 195px; height: 415px;
    background: var(--red); border-radius: 80px 60px 24px 24px;
  }
</style>
</head>
<body>
  <div class="spec-label">Width- 24” Height- 18”</div>

  <section class="magnet magnet--one">
    <div class="band band--navy-base"></div>
    <h1 class="title title--slab title--navy"><span class="line">KLAVO</span><span class="line">TOUR</span></h1>
    <p class="member-year">2026<sup>MEMBER</sup></p>
    <div class="golfer-art" role="img" aria-label="Red silhouette of a golfer putting a ball toward the hole"></div>
  </section>

  <section class="magnet magnet--two">
    <div class="band band--white-base"></div>
    <h2 class="title title--slab title--white"><span class="line">KLAVO</span><span class="line">TOUR</span></h2>
    <p class="member-line">2026 MEMBER</p>
    <div class="golfer-art" role="img" aria-label="Red silhouette of a golfer putting a ball toward the hole"></div>
  </section>

  <section class="magnet magnet--three">
    <div class="band band--white-short"></div>
    <div class="band band--navy-edge"></div>
    <h2 class="title title--sans title--white"><span class="line">KLAVO</span><span class="line">TOUR</span></h2>
    <p class="member-line">2026 MEMBER</p>
    <div class="golfer-art" role="img" aria-label="Red silhouette of a golfer putting a ball toward the hole"></div>
  </section>

  <section class="magnet magnet--four">
    <div class="band band--white-short"></div>
    <div class="band band--red-edge"></div>
    <h2 class="title title--sans title--white"><span class="line">KLAVO</span><span class="line">TOUR</span></h2>
    <p class="member-line">2026 MEMBER</p>
    <div class="golfer-art" role="img" aria-label="Red silhouette of a golfer putting a ball toward the hole"></div>
  </section>
</body>
</html>
```